Design a poster for popular Wine Bar in Melbourne

PROJECT: A1 poster and A4

JOB DESCRIPTION; We are a popular Wine Bar in Melbourne, a classy establishment that is serving the most extensive wine selection in our region. Check out our site: www.copperlanebar.com.au. We are looking for an "art nuevo" inspired poster, using bright block colours - please reference the example poster attached and this must as your inspiration and guide when designing the piece.

NAME OF EVENT: Amber Evenings

TAG LINE: “Choose more, try more, spend less and discover new wines"

WHATS GOING ON:
All our poured wines available by the half glass - 75ml
$5 cheese and charcuterie tasting plates.
$2 coffin Bay Oysters

WHEN:
Weekdays from 4pm -6pm
Saturdays from 2pm - 5pm

Look on the brighter side - your glass is half full.

VENUE INFORMATION:

Address; 42 Larkin St, Newport
Phone: 9472 6053
Email: info@copperlanebar.com.au
www.copperlanebar.com.au

Target Market(s)

25-50 lovers of fine wine and food

Industry/Entity Type

Event

Requirements
Must have
• The art nuevo styling much like the example poster we have attached. The company logo and all details of event must be represented. 2 block colours to be used and ensue the piece is high standard.

Images must be high resolution.

Poster must be completed in illustrator or photoshop

Ensure there is a 3mm internal and external bleed.
Should not have
• Images of people - we are wanting this to be a stylised piece using more abstract, artistic imagery in the styling referenced in the poster attached.

```html
<!DOCTYPE html>
<html lang="en">
<head>
<meta charset="utf-8">
<title>Amber Evenings – Poster</title>
<link rel="stylesheet" href="https://fonts.googleapis.com/css2?family=Great+Vibes&family=Italianno&family=Tinos&display=swap">
<style>
  :root {
    --ink: #000000;
    --paper: #ffffff;
    --wine: #d0142c;
    --wine-deep: #6e0512;
    --band-start: #f05a74;
    --band-mid: #e5173a;
    --band-end: #c80f2c;
  }
  html, body {
    margin: 0;
    padding: 0;
    overflow: hidden;
    background: var(--ink);
  }
  .poster {
    position: relative;
    width: 858px;
    height: 1200px;
    background: var(--ink);
    overflow: hidden;
    font-family: "Tinos", "Times New Roman", serif;
    color: var(--paper);
  }
  .hero-art {
    position: absolute;
    left: 0;
    top: 0;
    width: 858px;
    height: 760px;
    background:
      radial-gradient(ellipse 300px 150px at 340px 330px, rgba(208,20,44,0.85), rgba(110,5,18,0.55) 55%, rgba(0,0,0,0) 100%),
      radial-gradient(ellipse 480px 360px at 360px 300px, rgba(70,70,70,0.35), rgba(0,0,0,0) 75%);
  }
  .event-title {
    position: absolute;
    left: 0;
    top: 240px;
    width: 800px;
    margin: 0;
    font-family: "Great Vibes", cursive;
    font-weight: 400;
    line-height: 1;
    text-align: right;
  }
  .event-title .line-one {
    display: block;
    font-size: 150px;
    color: var(--paper);
    padding-right: 150px;
  }
  .event-title .line-two {
    display: block;
    font-size: 140px;
    color: var(--wine);
    margin-top: 10px;
  }
  .tagline {
    position: absolute;
    left: 0;
    top: 732px;
    width: 858px;
    margin: 0;
    text-align: center;
    font-family: "Italianno", cursive;
    font-size: 40px;
    color: var(--paper);
  }
  .details {
    position: absolute;
    right: 114px;
    top: 800px;
    width: 600px;
    text-align: right;
    font-size: 18px;
    line-height: 25px;
  }
  .details h2 {
    margin: 0;
    font-size: 17px;
    font-weight: 400;
    color: var(--wine);
  }
  .details p {
    margin: 0 0 8px;
  }
  .closing-line {
    position: absolute;
    right: 114px;
    top: 1034px;
    margin: 0;
    font-size: 21px;
    color: var(--paper);
  }
  .contact-band {
    position: absolute;
    left: 0;
    bottom: 0;
    width: 858px;
    height: 96px;
    background: linear-gradient(90deg, var(--band-start) 0%, var(--band-mid) 30%, var(--band-end) 100%);
  }
  .contact-band address {
    position: absolute;
    right: 114px;
    top: 16px;
    font-style: normal;
    text-align: right;
    color: var(--paper);
  }
  .contact-band .venue {
    display: block;
    font-size: 26px;
    line-height: 36px;
  }
  .contact-band .online {
    display: block;
    font-size: 19px;
    line-height: 28px;
  }
</style>
</head>
<body>
  <main class="poster">
    <div class="hero-art" role="img" aria-label="Close-up photograph of a tilted wine glass with red wine rippling as a drop falls into it"></div>

    <h1 class="event-title">
      <span class="line-one">Amber</span>
      <span class="line-two">Evenings</span>
    </h1>

    <p class="tagline">Choose more, try more, spend less and discover new wines</p>

    <section class="details">
      <h2>WHATS GOING ON:</h2>
      <p>All our poured wines available by the half glass - 75ml<br>
      $5 cheese and charcuterie tasting plates.<br>
      $2 coffin Bay Oysters</p>
      <h2>WHEN:</h2>
      <p>Weekdays from 4pm -6pm<br>
      Saturdays from 2pm - 5pm</p>
    </section>

    <p class="closing-line">Look on the brighter side - your glass is half full.</p>

    <footer class="contact-band">
      <address>
        <span class="venue">42 Larkin St, Newport • Phone: 9472 6053</span>
        <span class="online">info@copperlanebar.com.au • www.copperlanebar.com.au</span>
      </address>
    </footer>
  </main>
</body>
</html>
```